Kelvarine Pools

Luxury pool designer builder brochure

Company name is "Kelvarine"
Tag line is "Pools for the Mind Body & Soul"
Maybe integrate "Luxury Urban Lifestyle"

Target Market(s)

30 to 65 income of 200000.00 plus Affluent, high end life style
Luxury living

Industry/Entity Type

It Company

Font styles to use
Serif

Colors
000000

Requirements
Must have
• NOTE:
• Please remove the "Aquatic environments for the under the logo.
• I want a black background with a very contemporary feel.
• This is a luxury lifestyle product.

```html
<!DOCTYPE html>
<html lang="en">
<head>
<meta charset="utf-8">
<title>Kelvarine Pools – Brochure</title>
<link href="https://fonts.googleapis.com/css2?family=Open+Sans:wght@300;400&family=Yanone+Kaffeesatz:wght@300;400&display=swap" rel="stylesheet">
<style>
  :root {
    --black: #000000;
    --ink: #0b0b0b;
    --teal: #127f98;
    --mint: #6fd8c0;
    --white: #ffffff;
    --silver-light: #f4f4f4;
    --silver-dark: #c9c9c9;
    --stage: #d9d9d9;
    --text-dark: #111111;
  }
  * { margin: 0; padding: 0; box-sizing: border-box; }
  html, body { width: 1200px; height: 974px; overflow: hidden; }
  body {
    background: radial-gradient(ellipse at 50% 30%, #f2f2f2 0%, var(--stage) 80%);
    font-family: "Open Sans", Arial, sans-serif;
    position: relative;
  }
  .spread {
    position: absolute; left: 100px; top: 157px;
    width: 1000px; height: 660px;
    display: flex;
    box-shadow: 0 20px 40px rgba(0,0,0,.25);
  }
  .panel { position: relative; width: 500px; height: 660px; overflow: hidden; background: var(--black); }

  /* shared */
  .brand-name {
    font-family: "Open Sans", Arial, sans-serif; font-weight: 300;
    color: var(--white); letter-spacing: 2px;
  }
  .band-teal { position: absolute; left: 0; width: 100%; background: var(--teal); }
  .silver {
    position: absolute; left: 0; width: 100%; bottom: 0;
    background: linear-gradient(135deg, var(--silver-light) 0%, #e2e2e2 50%, var(--silver-dark) 100%);
  }
  .url { font-family: "Open Sans", Arial, sans-serif; color: var(--text-dark); letter-spacing: 1px; }

  /* back cover */
  .back-photo {
    position: absolute; left: 0; top: 0; width: 100%; height: 440px;
    background: linear-gradient(180deg, #2a2a2a 0%, #1a1a1a 45%, #070707 100%);
  }
  .back .brand-name { position: absolute; left: 150px; top: 170px; font-size: 38px; }
  .contact { position: absolute; left: 150px; top: 226px; width: 300px; text-align: center; }
  .contact .heading {
    font-family: "Yanone Kaffeesatz", sans-serif; font-weight: 300;
    color: var(--mint); font-size: 26px; letter-spacing: 1px; margin-bottom: 4px;
  }
  .contact p { color: var(--white); font-size: 11.5px; line-height: 18px; }
  .contact svg { width: 10px; height: 10px; vertical-align: -1px; margin-right: 5px; fill: var(--white); }
  .back .band-teal { top: 440px; height: 38px; }
  .back .silver { height: 182px; }
  .back .lifestyle {
    position: absolute; left: 0; width: 100%; top: 522px; text-align: center;
    font-family: "Yanone Kaffeesatz", sans-serif; font-weight: 300;
    font-size: 50px; color: var(--text-dark); letter-spacing: 1px;
  }
  .back .url { position: absolute; left: 0; width: 100%; top: 588px; text-align: center; font-size: 15px; }

  /* front cover */
  .front .brand-name { position: absolute; left: 0; width: 100%; top: 40px; text-align: center; font-size: 50px; }
  .tagline { position: absolute; left: 0; width: 100%; top: 124px; text-align: center; font-family: "Yanone Kaffeesatz", sans-serif; font-weight: 300; }
  .tagline .line-one { color: var(--white); font-size: 26px; letter-spacing: .5px; }
  .tagline .line-two { color: var(--mint); font-size: 38px; line-height: 36px; letter-spacing: .5px; }
  .front .band-teal { top: 222px; height: 36px; }
  .hero-photo {
    position: absolute; left: 0; top: 258px; width: 100%; height: 262px;
    background: linear-gradient(160deg, #3e4a38 0%, #7a6a58 35%, #2a8fbf 60%, #1f3a4a 100%);
  }
  .front .silver { height: 140px; }
  .thumbs { position: absolute; left: 20px; right: 20px; top: 470px; display: flex; justify-content: space-between; }
  .thumb { width: 142px; height: 92px; border: 5px solid var(--black); background: var(--black); box-shadow: 0 4px 8px rgba(0,0,0,.35); }
  .thumb span { display: block; width: 100%; height: 100%; }
  .thumb.one span { background: linear-gradient(180deg, #6d8db0 0%, #b77a56 60%, #2e8ab0 100%); }
  .thumb.two span { background: linear-gradient(180deg, #5e6a80 0%, #9a5a45 55%, #2a6f95 100%); }
  .thumb.three span { background: linear-gradient(180deg, #28402c 0%, #3a5a3a 50%, #7a9ad8 100%); }
  .front .url { position: absolute; left: 0; width: 100%; top: 608px; text-align: center; font-size: 15px; }
  .fold { position: absolute; left: 599px; top: 157px; width: 2px; height: 660px; background: rgba(0,0,0,.18); }
</style>
</head>
<body>
  <main class="spread">
    <section class="panel back">
      <div class="back-photo" role="img" aria-label="Dark night view of a luxury house beside a pool"></div>
      <div class="brand-name">Kelvarine</div>
      <div class="contact">
        <div class="heading">GET IN TOUCH</div>
        <p>Kelvarine Pools and Outdoors</p>
        <p><svg viewBox="0 0 10 10"><path d="M5 0a3.5 3.5 0 0 0-3.5 3.5C1.5 6 5 10 5 10s3.5-4 3.5-6.5A3.5 3.5 0 0 0 5 0zm0 5a1.5 1.5 0 1 1 0-3 1.5 1.5 0 0 1 0 3z"/></svg>4820 Larkmoor Court Ridgeway, Texas 77512</p>
        <p><svg viewBox="0 0 10 10"><path d="M2 0l2 2.5-1.2 1.3a6 6 0 0 0 3.4 3.4L7.5 6 10 8l-1.5 2C4 10 0 6 0 1.5z"/></svg>713.555.0187</p>
        <p><svg viewBox="0 0 10 10"><path d="M0 2h10v6H0z M0 2l5 3.5L10 2" fill="none" stroke="#fff" stroke-width="1"/></svg>design@kelvarineinc.com</p>
      </div>
      <div class="band-teal"></div>
      <div class="silver"></div>
      <div class="lifestyle">LUXURY URBAN LIFESTYLE</div>
      <div class="url">www.kelvarinepools.com</div>
    </section>

    <section class="panel front">
      <div class="brand-name">Kelvarine</div>
      <div class="tagline">
        <div class="line-one">POOLS FOR THE MIND BODY &amp; SOUL</div>
        <div class="line-two">LUXURY URBAN LIFESTYLE</div>
      </div>
      <div class="band-teal"></div>
      <div class="hero-photo" role="img" aria-label="Evening view of a lit pool with fire bowl beside a large house"></div>
      <div class="silver"></div>
      <div class="thumbs">
        <div class="thumb one"><span role="img" aria-label="Pool with stone steps and covered patio"></span></div>
        <div class="thumb two"><span role="img" aria-label="Infinity edge pool beside outdoor lounge"></span></div>
        <div class="thumb three"><span role="img" aria-label="Garden pool lit at night"></span></div>
      </div>
      <div class="url">www.kelvarinepools.com</div>
    </section>
  </main>
  <div class="fold"></div>
</body>
</html>
```